Business card for Full Stable Care Vandorpe

I would like to have me designed an professional business card with my existing logo for my company called : full stable care vandorpe gcv.
I prefer a two sided business card with on the back side only the horses head and the website : fscvandorpe-example.eu
Only one colour shouldbe all right.
The logo must appear in a nic professional way on the business card.

Other suggestion are welcome.

All copy wrights must be released by the designer after we have selected a final design.

Target Market(s)

Equestrian businesses

Industry/Entity Type

Business

Contact Information for Business Card

Laurent Vandorpe
Title: zaakvoerder
Full Stable Care Vandorpe GCV
Molkenweg 47
B - 3190 Heidelaar
België
Phone: + 32 491 68 27 04
Mail: laurent@fscvandorpe-example.eu

Font styles to use
Serif

Requirements
Must have
• My own logo
• See attached files
• Website: fscvandorpe-example.eu

```html
<!DOCTYPE html>
<html lang="nl">
<head>
<meta charset="utf-8">
<title>Full Stable Care Vandorpe – Business Card</title>
<link href="https://fonts.googleapis.com/css2?family=Tinos:wght@400;700&display=swap" rel="stylesheet">
<style>
  :root {
    --backdrop: #2b2b2b;
    --card-dark: #151314;
    --card-light: #ffffff;
    --ink-light: #e8e6e6;
    --ink-dark: #111111;
  }
  * { margin: 0; padding: 0; box-sizing: border-box; }
  html, body { width: 1200px; height: 716px; overflow: hidden; }
  body {
    background: var(--backdrop);
    font-family: "Tinos", "Times New Roman", serif;
    position: relative;
  }
  .card {
    position: absolute;
    width: 500px;
    height: 290px;
    top: 213px;
    box-shadow: 0 10px 28px rgba(0,0,0,.45);
  }
  .card--back {
    left: 70px;
    background: var(--card-dark);
    color: var(--ink-light);
  }
  .card--front {
    left: 630px;
    background: var(--card-light);
    color: var(--ink-dark);
    display: flex;
    align-items: center;
    justify-content: center;
  }
  .brand-mark {
    position: absolute;
    left: 60px;
    top: 88px;
    width: 96px;
    height: 96px;
    border-radius: 50%;
    background: var(--ink-light);
  }
  .contact {
    position: absolute;
    left: 200px;
    top: 62px;
    font-size: 14px;
    line-height: 1.3;
  }
  .contact__name {
    font-size: 17px;
    text-transform: uppercase;
    letter-spacing: .02em;
  }
  .contact__title { margin-bottom: 20px; }
  .contact__lines { margin-bottom: 14px; }
  .brand-name {
    display: flex;
    align-items: center;
    gap: 16px;
    font-size: 30px;
    font-weight: 700;
    letter-spacing: .01em;
  }
  .brand-name__dot {
    width: 40px;
    height: 40px;
    border-radius: 50%;
    background: var(--ink-dark);
  }
</style>
</head>
<body>
  <section class="card card--back">
    <div class="brand-mark" aria-hidden="true"></div>
    <div class="contact">
      <p class="contact__name">Laurent Vandorpe</p>
      <p class="contact__title">Director</p>
      <div class="contact__lines">
        <p>+ 32 491 68 27 04</p>
        <p>laurent@fscvandorpe-example.eu</p>
        <p>www.fscvandorpe-example.eu</p>
      </div>
      <p>Molkenweg 47</p>
      <p>B - 3190 Heidelaar</p>
      <p>België</p>
    </div>
  </section>
  <section class="card card--front">
    <div class="brand-name">
      <span class="brand-name__dot" aria-hidden="true"></span>
      <span>Full Stable Care Vandorpe</span>
    </div>
  </section>
</body>
</html>
```